RT Consult - Web Design Upgrade

We have recently designed a website (http://www.rtconsult-demo.com.au) which requires more creative and professional inputs. The website was designed using 'jolly portals site builder template' and it is currently available for viewing on the internet. Also, you are able to access the PDF files for the 6 main pages (i.e. Home, About, Services, Contaminated Land Management, Groundwater Management and Contact).

The current website has 17 pages, however, your design may only be required for the 6 main pages.

Currently the website background is white but we are open to other colours provided the company logo is adjusted accordingly.

The idea is to upgrade the existing design and, if possible, continue using 'jolly portals' as the preferred web host. So we are not sure if the design should be coded or uncoded...we leave it to your proficiency and advice.

Target Market(s)

Government organisations, landowners and developers, waste and utilities companies, community organisations and individuals.

Industry/Entity Type

Internet

Number of Pages Required

5+ page

Font styles to use
Sans Serif

Colors
0355a3
3176b5
9ccb3b
acd037
ffffff

Requirements
Nice to have
• Sliding images

```html
<!DOCTYPE html>
<html lang="en">
<head>
<meta charset="utf-8">
<title>RT Consult – Home</title>
<link href="https://fonts.googleapis.com/css2?family=Arimo:wght@400;700&display=swap" rel="stylesheet">
<style>
  :root {
    --blue: #0355a3;
    --blue-mid: #3176b5;
    --green: #9ccb3b;
    --green-alt: #acd037;
    --white: #ffffff;
    --navy-text: #1e3f73;
    --band: #ececec;
    --dot-off: #bdbdbd;
  }
  * { margin: 0; padding: 0; box-sizing: border-box; }
  html, body { width: 1200px; height: 1100px; overflow: hidden; }
  body {
    position: relative;
    background: var(--white);
    font-family: "Arimo", Arial, sans-serif;
  }

  /* Header */
  .site-header { position: absolute; left: 0; top: 0; width: 1200px; height: 125px; }
  .brand {
    position: absolute; left: 122px; top: 30px;
    display: flex; align-items: center; gap: 12px;
  }
  .brand-dot {
    width: 48px; height: 48px; border-radius: 50%;
    background: var(--blue);
  }
  .brand-name {
    font-size: 26px; font-weight: 700; color: var(--blue);
    letter-spacing: 0.5px;
  }
  .tagline {
    position: absolute; right: 122px; top: 49px;
    font-size: 26px; color: var(--green); letter-spacing: 1.2px;
  }

  /* Navigation */
  .main-nav {
    position: absolute; left: 0; top: 125px; width: 1200px; height: 60px;
    background: var(--blue);
  }
  .nav-item {
    position: absolute; top: 0; height: 60px; line-height: 57px;
    font-size: 17px; font-weight: 700; color: var(--white);
    text-align: center; letter-spacing: 0.4px;
  }
  .nav-item.is-active { background: var(--green); }
  .search {
    position: absolute; left: 739px; top: 14px; width: 340px; height: 28px;
    background: var(--white); border-radius: 7px; overflow: hidden;
  }
  .search-field {
    position: absolute; left: 11px; top: 6px;
    font-size: 14px; font-style: italic; color: #555; letter-spacing: 0.4px;
  }
  .search-go {
    position: absolute; right: 0; top: 0; width: 71px; height: 28px;
    background: var(--green); border-radius: 7px;
    color: var(--white); font-size: 14px; font-weight: 700;
    text-align: center; line-height: 28px;
  }

  /* Slider */
  .slider-band {
    position: absolute; left: 0; top: 185px; width: 1200px; height: 560px;
    background: var(--band);
  }
  .slide {
    position: absolute; left: 120px; top: 12px; width: 960px; height: 535px;
    border: 2px solid var(--white);
    background:
      radial-gradient(ellipse at 70% 65%, #b6f03a 0%, #6fbd1d 30%, transparent 60%),
      linear-gradient(160deg, #0c1a06 0%, #264f0b 35%, #5aa516 60%, #2c6a0c 85%, #143407 100%);
  }
  .slide-caption {
    position: absolute; left: 565px; top: 368px; width: 391px; height: 110px;
    background: rgba(0, 0, 0, 0.35);
    padding: 29px 0 0 39px;
    font-size: 21px; font-weight: 700; color: var(--white);
    line-height: 24px; letter-spacing: 0.9px;
  }
  .slider-dots {
    position: absolute; left: 551px; top: 759px;
    display: flex; gap: 4px;
  }
  .slider-dot { width: 15px; height: 15px; border-radius: 50%; background: var(--blue-mid); }
  .slider-dot.is-current { background: var(--dot-off); }

  /* Intro */
  .intro {
    position: absolute; left: 178px; top: 806px;
    font-size: 25px; line-height: 29px; color: var(--navy-text);
    letter-spacing: 1.3px;
  }

  /* Footer */
  .footer-band {
    position: absolute; left: 0; top: 991px; width: 1200px; height: 109px;
    background: var(--band);
  }
  .site-footer {
    position: absolute; left: 121px; top: 13px; width: 958px; height: 96px;
    background: var(--blue); color: var(--white);
  }
  .legal {
    position: absolute; left: 24px; top: 16px;
    font-size: 14px; line-height: 17px; letter-spacing: 0.6px;
  }
  .footer-nav {
    position: absolute; right: 29px; top: 34px;
    font-size: 15px; font-weight: 700; letter-spacing: 0.5px; word-spacing: 3px;
  }
  .footer-nav .sep { margin: 0 6px; }
</style>
</head>
<body>
  <header class="site-header">
    <div class="brand">
      <span class="brand-dot"></span>
      <span class="brand-name">RT Consult</span>
    </div>
    <p class="tagline">”Working to Sustain our Environments”</p>
  </header>

  <nav class="main-nav">
    <span class="nav-item is-active" style="left:147px;width:100px;">Home</span>
    <span class="nav-item" style="left:263px;width:80px;">About</span>
    <span class="nav-item" style="left:377px;width:90px;">Services</span>
    <span class="nav-item" style="left:487px;width:80px;">Contact</span>
    <div class="search">
      <span class="search-field">Search...</span>
      <span class="search-go">Go</span>
    </div>
  </nav>

  <section class="slider-band">
    <div class="slide" role="img" aria-label="Close-up photograph of green grass blades with water droplets">
      <p class="slide-caption">Purchase / Sale contamination<br>Appraisal</p>
    </div>
  </section>

  <div class="slider-dots">
    <span class="slider-dot"></span>
    <span class="slider-dot"></span>
    <span class="slider-dot is-current"></span>
    <span class="slider-dot"></span>
    <span class="slider-dot"></span>
    <span class="slider-dot"></span>
  </div>

  <p class="intro">We implement techinal leadership in our approach, promote<br>excellent in our services and support practical solutions</p>

  <div class="footer-band">
    <footer class="site-footer">
      <p class="legal">Copyright&nbsp; 2014 - Rock &amp; Terrain Consulting Pty Ltd<br>Also trading as RT Consult - All rights reserved<br>ABN 12 345 678 901</p>
      <p class="footer-nav">Home <span class="sep">/</span> About <span class="sep">/</span> Services <span class="sep">/</span>Contact</p>
    </footer>
  </div>
</body>
</html>
```